business card for law firm that reflects the web site -www.MarenHolt.com. That is pleasant to read

We need a business card for a small law firm. Your company designed our logo - tree of life - which I can provide to the designers. The card should be on both sides. Use the coloring from the web site (www.MarenHolt.com) and logo (I have several formats). I am attaching the logo, but not sure what format to use.

First side name of firm: Law Office of M.K. Holt, P.A. 4816 West Sorrelwood, Suite 300, Phoenix, AZ 85019, Phone: 602.555.0143, Fax: 602.555.0187, web site: www.MarenHolt.com, email: MHolt@MarenHolt.com.
Maren K. Holt Bankruptcy and Foreclosure Attorney & Counselor.
Back side (perhaps vertical) the logo and then Notes with lines. At the bottom: Proud to help people and small businesses file for bankruptcy protection. We are a debt relief agency.
Updates

I have several versions of the logo. Will be happy to share whatever you need. Added Sunday, April 3, 2016

Target Market(s)

everyone

Industry/Entity Type

Legal

Contact Information for Business Card

I prefer something unique (rounded edges, design that adopts my web site - www.MarenHolt.com.

Font styles to use
Serif

Requirements
Must have
• First side name of firm: Law Office of M.K. Holt, P.A. 4816 West Sorrelwood, Suite 300, Phoenix, AZ 85019, Phone: 602.555.0143, Fax: 602.555.0187, web site: www.MarenHolt.com, email: MHolt@MarenHolt.com.
• Maren K. Holt Bankruptcy and Foreclosure Attorney & Counselor.
• Back side (perhaps vertical) the logo and then Notes with lines. At the bottom: Proud to help people and small businesses file for bankruptcy protection. We are a debt relief agency.
• Green and brown colors that reflect the web site: www.MarenHolt.com
Should not have
• Type so small that older people cannot read.

```html
<!DOCTYPE html>
<html lang="en">
<head>
<meta charset="utf-8">
<title>Law Office of M.K. Holt, P.A. – Business Card</title>
<link rel="stylesheet" href="https://fonts.googleapis.com/css2?family=Open+Sans:wght@400;600;700&display=swap">
<style>
  :root {
    --forest: #0d4a14;
    --forest-deep: #0a3f10;
    --leaf: #1f5e22;
    --bark: #4a2a1c;
    --ink: #3b3b3b;
    --paper: #ffffff;
    --backdrop: #e9e6e1;
  }
  * { box-sizing: border-box; margin: 0; padding: 0; }
  html, body {
    width: 1200px; height: 900px; overflow: hidden;
    background: var(--backdrop);
    font-family: "Open Sans", Arial, sans-serif;
  }
  .sheet {
    width: 1200px; height: 900px;
    display: flex; flex-direction: column;
    align-items: center; justify-content: center; gap: 40px;
  }
  .card {
    position: relative;
    width: 700px; height: 400px;
    background: var(--paper);
    overflow: hidden;
    box-shadow: 0 6px 18px rgba(0,0,0,0.18);
  }

  /* Back side */
  .card-back .field {
    position: absolute; left: 0; top: 0; width: 100%; height: 248px;
    background: var(--forest);
  }
  .card-back .emblem {
    position: absolute; left: 50%; top: 24px; transform: translateX(-50%);
    width: 200px; height: 200px; border-radius: 50%;
    border: 3px solid rgba(255,255,255,0.07);
    display: flex; align-items: center; justify-content: center;
    color: rgba(255,255,255,0.09);
    font-weight: 700; font-size: 26px;
  }
  .card-back .rule {
    position: absolute; left: 0; width: 100%; height: 10px; top: 256px;
    background: var(--forest);
  }
  .card-back .tagline {
    position: absolute; left: 0; top: 266px; width: 100%; height: 72px;
    display: flex; align-items: center; justify-content: center;
    text-align: center;
    color: var(--forest); font-weight: 700; font-size: 17px; line-height: 1.35;
  }
  .card-back .footer-band {
    position: absolute; left: 0; bottom: 0; width: 100%; height: 62px;
    background: var(--forest);
  }

  /* Front side */
  .card-front .seal {
    position: absolute; left: 70px; top: 150px;
    width: 200px; height: 200px; border-radius: 50%;
    border: 8px solid var(--bark);
    display: flex; align-items: center; justify-content: center;
    text-align: center;
    color: var(--forest); font-weight: 700; font-size: 22px; line-height: 1.25;
  }
  .card-front .details {
    position: absolute; left: 372px; top: 44px; width: 310px;
    color: var(--ink);
  }
  .attorney-name { color: var(--forest); font-weight: 700; font-size: 21px; line-height: 1.15; }
  .attorney-title { font-size: 13.5px; line-height: 1.3; margin-top: 2px; }
  .firm-name { color: var(--forest); font-weight: 600; font-size: 16px; margin-top: 16px; margin-left: 32px; }
  .firm-address { font-size: 14px; line-height: 1.5; margin-top: 2px; margin-left: 32px; font-style: normal; }
  .contact-list { list-style: none; margin-top: 22px; margin-left: 72px; }
  .contact-list li { display: flex; align-items: center; gap: 10px; font-size: 14.5px; line-height: 1.6; }
  .contact-list svg { width: 13px; height: 13px; fill: var(--forest); flex: none; }
</style>
</head>
<body>
<main class="sheet">

  <section class="card card-back" aria-label="Business card, back">
    <div class="field"></div>
    <div class="emblem">M.K. Holt</div>
    <div class="rule"></div>
    <p class="tagline">Proud to help people and small businesses file for<br>bankruptcy protection. We are a debt relief agency.</p>
    <div class="footer-band"></div>
  </section>

  <section class="card card-front" aria-label="Business card, front">
    <div class="seal">Law Office of<br>M.K. Holt</div>
    <div class="details">
      <h1 class="attorney-name">Maren K. Holt</h1>
      <p class="attorney-title">Bankruptcy and Foreclosure<br>Attorney &amp; Counselor</p>
      <h2 class="firm-name">Law Office of M.K. Holt</h2>
      <address class="firm-address">P.A. 4816 West Sorrelwood,<br>Suite 300, Phoenix, AZ 85019</address>
      <ul class="contact-list">
        <li>
          <svg viewBox="0 0 16 16" aria-hidden="true"><path d="M3.5 1l2.5 3-1.5 1.8c.9 2 2.4 3.5 4.4 4.4L10.7 8.7l3 2.5-1.2 2.8C7 14 2 9 2 2.5z"/></svg>
          602.555.0143
        </li>
        <li>
          <svg viewBox="0 0 16 16" aria-hidden="true"><path d="M4 1h6l2 2v3h2v9H2V6h2zm1 1v4h6V3.5L9.5 2zM4 9v2h2V9zm3 0v2h2V9zm3 0v2h2V9z"/></svg>
          602.555.0187
        </li>
        <li>
          <svg viewBox="0 0 16 16" aria-hidden="true"><path d="M1 3h14v10H1zm1.5 1.2V5l5.5 4 5.5-4v-.8z"/></svg>
          www.MarenHolt.com
        </li>
        <li>
          <svg viewBox="0 0 16 16" aria-hidden="true"><circle cx="8" cy="8" r="7"/></svg>
          MHolt@MarenHolt.com
        </li>
      </ul>
    </div>
  </section>

</main>
</body>
</html>
```